KVRo Business Cards

We need a business card design. We are a Technology (Audio Visual) design, sales and installation company. Looking for a double sided design, clean

Contact Information for Business Card

Clean, modern look, 2 sided

Font styles to use
Sans Serif

```html
<!DOCTYPE html>
<html lang="en">
<head>
<meta charset="utf-8">
<title>KVRo Business Cards</title>
<link href="https://fonts.googleapis.com/css2?family=Lexend:wght@300;400;500;700&family=Roboto:wght@400;700&display=swap" rel="stylesheet">
<style>
  :root {
    --navy: #172d3c;
    --orange: #de8522;
    --paper: #ebe8ea;
    --ink: #1c2a33;
    --backdrop: #c28a3c;
    --white: #f4f2f2;
  }
  * { margin: 0; padding: 0; box-sizing: border-box; }
  html, body { width: 1200px; height: 1101px; overflow: hidden; }
  body {
    background: var(--backdrop);
    position: relative;
    font-family: "Lexend", sans-serif;
  }
  .card {
    position: absolute;
    width: 303px;
    height: 530px;
    box-shadow: 0 14px 30px rgba(60, 25, 0, 0.35);
  }
  .card-front { left: 246px; top: 269px; background: var(--paper); }
  .card-back { left: 642px; top: 267px; background: var(--navy); }

  .front-logo {
    position: absolute; left: 0; right: 0; top: 30px;
    text-align: center;
    font-family: "Lexend", sans-serif;
    font-weight: 700;
    font-size: 88px;
    letter-spacing: -2px;
    color: var(--navy);
    line-height: 1;
  }
  .name-band {
    position: absolute; left: 0; right: 0; top: 162px; height: 93px;
    background: var(--navy);
    text-align: center;
    color: var(--white);
  }
  .person-name {
    font-family: "Roboto", sans-serif;
    font-weight: 700;
    font-size: 21px;
    margin-top: 25px;
    letter-spacing: 0.2px;
  }
  .person-role {
    font-weight: 300;
    font-size: 16px;
    margin-top: 4px;
    letter-spacing: 0.5px;
  }
  .contact-panel {
    position: absolute; left: 0; right: 0; top: 273px; height: 239px;
    background: var(--orange);
    text-align: center;
    color: var(--ink);
  }
  .divider { position: absolute; left: 0; top: 0; }
  .contact-lines {
    position: absolute; left: 0; right: 0; top: 72px;
    font-weight: 500; font-size: 17px; line-height: 21px;
    letter-spacing: 0.3px;
  }
  .address-lines {
    position: absolute; left: 0; right: 0; top: 170px;
    font-weight: 500; font-size: 15px; line-height: 21px;
    letter-spacing: 0.2px;
  }

  .back-lockup {
    position: absolute; left: 72px; top: 212px;
    color: var(--white);
  }
  .back-www { font-size: 21px; font-weight: 400; letter-spacing: 1px; line-height: 1; }
  .back-logo {
    font-weight: 700; font-size: 74px; letter-spacing: -2px;
    line-height: 1; margin-top: -2px;
  }
  .back-tld {
    font-size: 19px; font-weight: 400; letter-spacing: 0.5px;
    text-align: right; line-height: 1; margin-top: -2px;
  }
</style>
</head>
<body>
  <section class="card card-front">
    <div class="front-logo">KVRo</div>
    <div class="name-band">
      <div class="person-name">MARCUS ELLERY</div>
      <div class="person-role">Manager</div>
    </div>
    <div class="contact-panel">
      <svg class="divider" width="303" height="239" viewBox="0 0 303 239">
        <g stroke="var(--ink)" stroke-width="1.5">
          <line x1="52" y1="51" x2="114" y2="51"/>
          <line x1="191" y1="51" x2="253" y2="51"/>
          <line x1="52" y1="152" x2="130" y2="152"/>
          <line x1="173" y1="152" x2="253" y2="152"/>
        </g>
        <!-- phone -->
        <circle cx="135" cy="51" r="11" fill="var(--paper)"/>
        <path d="M130.5 45.5 l2.5 -0.5 l1.5 3.2 l-1.6 1.2 a8 8 0 0 0 3.7 3.7 l1.2 -1.6 l3.2 1.5 l-0.5 2.5 a9.5 9.5 0 0 1 -10 -10 z" fill="var(--ink)"/>
        <!-- mail -->
        <circle cx="169" cy="51" r="11" fill="var(--paper)"/>
        <rect x="162.5" y="46.5" width="13" height="9" rx="1" fill="var(--ink)"/>
        <path d="M162.5 47 l6.5 4.5 l6.5 -4.5" fill="none" stroke="var(--paper)" stroke-width="1.2"/>
        <!-- pin -->
        <circle cx="151.5" cy="152" r="11.5" fill="var(--ink)"/>
        <path d="M151.5 158.5 l-4 -6 a4.6 4.6 0 1 1 8 0 z" fill="var(--paper)"/>
        <circle cx="151.5" cy="150" r="1.8" fill="var(--ink)"/>
      </svg>
      <div class="contact-lines">
        <div>014 628 3170</div>
        <div>hello@kvro.tech</div>
      </div>
      <div class="address-lines">
        <div>1830 Linden Row Suite 200</div>
        <div>Ashford, Ohio 40216</div>
      </div>
    </div>
  </section>

  <section class="card card-back">
    <div class="back-lockup">
      <div class="back-www">WWW.</div>
      <div class="back-logo">KVRo</div>
      <div class="back-tld">.TECH</div>
    </div>
  </section>
</body>
</html>
```